Small business offering independent forensic science consultancy requires flyer and magnet design

We had great success in obtaining a logo design using pixel harbor and we are hoping to draw on your expertise again!

Clearwater Evidence Advisors is a small consultancy business that mainly involves reviewing forensic case files for both the prosecution and defence, and providing expert opinion on the findings in the form of a report, as well as attending court as an expert witness.

Our areas of expertise currently is Forensic Biology (analysis of body fluids), DNA analysis and bloodstain pattern analysis, but this may grow in the future. You can find further information as well as obtain a bit of a feel for the style we are looking for from our website www.clearwaterevidenceadvisors.com.au.

The flyer should be clean and professional looking and we have attached files including our logo and and a Plumtree Text Doc containing the wording for inclusion in the flyer. We have attached an 'ímage feel' document to give you a feel for the types of images we like - but we own all the images on our website, so please contact me if you want to use any of these images and I can send you the files - however are open to any other images in keeping with our website and brand feel.

We will consider various format options such as tri-fold, bi-fold, however,DL sized bi-fold is probably a slight preference. We are also open to suggestions from designers. We would also like to have the capability to modify our wording on the flyer as we have not completely locked it in as yet.

Please note that the brief is also to include the design of a simple advertising magnet to supplement our flyers. They will also be given out separately. The magnet should be a simple design for standard size (90mm x 45mm) magnet, similar to a business card with logo, tagline and contact details (information contained in attached file).

We look forward to seeing your design ideas. Thanks!
Updates

We will be extending the deadline for this project to the 10th January, to allow designers plenty of time given the time of year! 

Thanks to all the designers who have submitted designs so far - as it is the Christmas and New Year period, I will be extending the deadline by one week to allow time for all of you who have accepted my invitation to submit a design.

We will provide individual feedback over the next week to those who have submitted designs. 

We've had some great designs so far - and look forward to seeing some more!

Many thanks!

Hi designers - thanks for the designs submitted so far.  We have provided feedback to all designs under consideration - and welcome re-submissions with the alterations we have suggested.

The deadline will stay at the 10th Jan, so please finalise your designs and re-submit before this date.

We are also still open to considering new designs at this stage.

Kind regards

Marta

Target Market(s)

The criminal law and law enforcement communities including solicitors, barristers, and detectives.

Industry/Entity Type

Advertising

Requirements
Must have
• Clearwater Evidence Advisors Logo
Clearwater Evidence Advisors Tagline
At least one of the images from our website
Nice to have
• Other images that fit with the picture scheme on our website and in the reference pictures attached.
Should not have
• pictures of fingerprints, deceased, glamorised crime scenes, police or vbq references.

```html
<!DOCTYPE html>
<html lang="en">
<head>
<meta charset="utf-8">
<title>Clearwater Evidence Advisors – Bi-fold Flyer</title>
<link href="https://fonts.googleapis.com/css2?family=Open+Sans:ital,wght@0,400;0,600;0,700;1,400&display=swap" rel="stylesheet">
<style>
  :root{
    --backdrop:#d9d9d9;
    --paper:#ffffff;
    --sky:#4ec4e8;
    --teal:#3aa6c6;
    --brand:#2c6fb1;
    --ink:#4a4f55;
    --muted:#6d7379;
    --ice-1:#e6f5fc;
    --ice-2:#bfe3f4;
    --violet-1:#6a4fa8;
    --violet-2:#c58fc9;
  }
  *{box-sizing:border-box;margin:0;padding:0}
  html,body{width:1200px;height:800px;overflow:hidden}
  body{background:var(--backdrop);font-family:"Open Sans",Arial,sans-serif;color:var(--ink);position:relative}

  .spread{position:absolute;top:215px;width:540px;height:370px;display:flex;box-shadow:0 6px 18px rgba(0,0,0,.18)}
  .spread--outside{left:40px}
  .spread--inside{left:620px}
  .page{position:relative;width:270px;height:370px;background:var(--paper);overflow:hidden}
  .page + .page{border-left:1px solid #e3e3e3}

  .brand{display:flex;align-items:center;gap:6px;color:var(--brand);font-weight:600;font-size:11px;line-height:1.1}
  .brand__dot{width:14px;height:14px;border-radius:50%;background:var(--brand);flex:none}

  .molecule-field{position:absolute;left:0;right:0;bottom:0;height:80px;background:linear-gradient(180deg,var(--paper),var(--ice-1) 35%,var(--ice-2))}

  /* back cover */
  .who-band{position:absolute;left:0;top:0;width:100%;height:122px;background:var(--sky);color:#fff;padding:40px 16px 0 26px;font-size:5.5px;line-height:1.4}
  .who-band h3{font-size:7px;font-weight:700;margin-bottom:2px}
  .who-band ul{margin:3px 0 0 12px}
  .tube-strip{position:absolute;left:0;top:122px;width:100%;height:50px;background:linear-gradient(90deg,var(--violet-1),var(--violet-2),var(--violet-1))}
  .contact{position:absolute;left:0;top:200px;width:100%;text-align:center;font-size:5.5px;line-height:1.5;font-style:italic;z-index:1}
  .contact .brand{justify-content:center;font-style:normal;margin-bottom:4px}
  .contact h4{font-size:6.5px;font-style:normal;font-weight:600}

  /* front cover */
  .front-brand{position:absolute;left:45px;top:40px}
  .collage{position:absolute;left:45px;top:75px;width:180px;height:175px;background:linear-gradient(135deg,#e9eef2,#b8c6d0 55%,#dfe6eb)}
  .title-band{position:absolute;left:0;bottom:0;width:100%;height:110px;background:var(--teal);color:#fff;text-align:center;padding-top:22px;font-weight:700;font-size:10.5px;line-height:1.55}

  /* inside left */
  .inside-band{position:absolute;left:0;top:0;width:100%;height:95px;background:var(--teal)}
  .lab-photo{position:absolute;left:110px;top:10px;width:160px;height:165px;background:linear-gradient(135deg,#cfe4f1,#7fa7c4 50%,#a98bc9)}
  .areas{position:absolute;left:16px;top:195px;width:240px;font-size:5.5px;line-height:1.5}
  .areas ul{margin:3px 0 0 12px}
  .thumb{position:absolute;top:238px;height:38px;width:62px}
  .thumb--dna{left:134px;background:linear-gradient(135deg,#e9d3d6,#b9434f)}
  .thumb--gel{left:200px;background:linear-gradient(135deg,#2d3f7c,#b0506a)}

  /* inside right */
  .ability{position:absolute;left:14px;top:18px;width:245px;font-size:5.2px;line-height:1.45}
  .ability h3{color:var(--brand);font-size:6.5px;font-weight:700;margin-bottom:2px}
  .ability ul{margin-left:10px}
  .ability li{margin-bottom:2px}
  .ability li.narrow{width:125px}
  .scope-photo{position:absolute;left:155px;top:75px;width:105px;height:85px;background:linear-gradient(135deg,#b55bb8,#5a3f9c 55%,#2e3c7a)}
  .col{position:absolute;top:168px;width:112px;font-size:5.3px;line-height:1.5}
  .col p{margin-bottom:5px}
  .col--a{left:14px}
  .col--b{left:145px}
</style>
</head>
<body>

<section class="spread spread--outside">
  <article class="page page--back">
    <div class="who-band">
      <h3>Who Uses Us?</h3>
      <p>Our independent services are trusted by legal professionals across Australia who need clear scientific advice on their cases, including:</p>
      <ul>
        <li>Defence law firms</li>
        <li>Legal Aid</li>
        <li>Prosecution legal teams</li>
        <li>Universities</li>
      </ul>
    </div>
    <div class="tube-strip" role="img" aria-label="Row of laboratory test tubes in violet light"></div>
    <div class="contact">
      <div class="brand"><span class="brand__dot"></span>Clearwater Evidence Advisors</div>
      <h4>Contact Us</h4>
      <p>Phone: +61 2 9555 0148</p>
      <p>Email: enquiries@clearwaterevidenceadvisors.com.au</p>
      <p>Web: www.clearwaterevidenceadvisors.com.au</p>
      <p>Mail: PO Box 418 Riverbend NSW Australia 2999</p>
    </div>
    <div class="molecule-field" role="img" aria-label="Soft blue molecular hexagon pattern"></div>
  </article>

  <article class="page page--front">
    <div class="brand front-brand"><span class="brand__dot"></span>Clearwater Evidence Advisors</div>
    <div class="collage" role="img" aria-label="Grid of photos showing scientists working in a laboratory"></div>
    <div class="title-band">Forensic Science Expertise<br>From The Crime Scene To Court</div>
  </article>
</section>

<section class="spread spread--inside">
  <article class="page page--inside-left">
    <div class="inside-band"></div>
    <div class="lab-photo" role="img" aria-label="Scientist looking through a microscope in a laboratory"></div>
    <div class="areas">
      <p>We offer specialist expertise in the following areas:</p>
      <ul>
        <li>Forensic biology</li>
        <li>DNA analysis and collection techniques</li>
        <li>Bloodstain pattern analysis</li>
      </ul>
    </div>
    <div class="thumb thumb--dna" role="img" aria-label="Red DNA strand illustration"></div>
    <div class="thumb thumb--gel" role="img" aria-label="DNA profile bands"></div>
    <div class="molecule-field" role="img" aria-label="Soft blue molecular hexagon pattern"></div>
  </article>

  <article class="page page--inside-right">
    <div class="ability">
      <h3>We have the ability to:</h3>
      <ul>
        <li>Conduct an independent review of the work conducted by the State or Federal laboratories</li>
        <li>Assess if all appropriate examinations have been conducted on the evidence</li>
        <li>Provide an expert opinion in relation to the significance of the evidence</li>
        <li class="narrow">Assist in providing appropriate lines of questioning for expert witnesses</li>
        <li class="narrow">Appear in court as an expert witness</li>
        <li class="narrow">Perform laboratory based examinations or re-examinations of items for biological evidence</li>
        <li class="narrow">Conduct bespoke training on forensic biology, DNA analysis and interpretation and forensic science</li>
      </ul>
    </div>
    <div class="scope-photo" role="img" aria-label="Microscope under violet laboratory light"></div>
    <div class="col col--a">
      <p>We will provide high quality and timely advice that is honest and transparent and any resulting reports will be presented in a form readily understood by non-scientific audiences.</p>
      <p>Clearwater Evidence Advisors has implemented a quality framework and is structured to provide a consistent technical review process. All staff hold accreditation with relevant bodies and we continually work to expand our services and ensure our work is of the highest quality.</p>
    </div>
    <div class="col col--b">
      <p>We believe our experience from the crime scene to the court and our quality framework offers our clients one of the most comprehensive independent forensic services available in the area of forensic biology and DNA analysis.</p>
    </div>
    <div class="molecule-field" role="img" aria-label="Soft blue molecular hexagon pattern"></div>
  </article>
</section>

</body>
</html>
```